依頼詳細
●当社ホームページhttp://tmrv-example.jp/をご覧頂くと、現在の総合カタログNO.50の表紙がご覧になれます。HP内のコンテンツは使って下さっても構いませんが、今までとは違ったものを期待しています。シンプルかつ落ち着いていて、さらには豪華に見えるものを希望します。当社は造花でも特に仏花など宗教造花の割合が多目です。しかしデザインは宗教造花にこだわらないようにしてください。ステキな作品の応募をお待ちしております。

●表裏のデザインですが、裏表紙はデザインの都合で無地でも構いません。背表紙はありません。

●今回は52号です。表表紙のどこかに号数をお入れください。

A4
4ページ
補足説明
●ページ数の欄が4ページとなっています。ポルタミクさんの入力方式でカタログ・パンフレットを選択した場合4ページ以上の選択しかできないためです。実際は表ページのみ1ページ、もしくは表裏ページの2ぺージです。
●50号の表裏表紙のデザインは添付ファイルをご覧ください。当社のロゴと社名、住所はこちらで入れます。
●繰り返しますがお願いするのは表裏表紙のみです。
■ 選んだ理由

1作品目は、ステンドグラス風に加工した、今まで当社のカタログにない斬新な
イメージで、選びました。
2作品目は、蝶が舞うお花畑のようなイメージで、やさしさが伝わってくる感じで選びました。

■ 提案者全員のお礼・コメント

この度は、フラワーカタログ表紙デザインに多数の御提案を頂き、誠にありがとうございました。
どれも素晴らしい作品ばかりで、当社のキャッチフレーズを随所に使用した作品や、斬新なデザイン、複数の御提案を頂いた方、一人一人の思いが込められており、選考に時間がかかりました。
社内で、厳選なる審査の結果、1作品を選ぶ予定でしたが、今回は、2名様の当選としました。
今回残念ながら、当選されなかった方々には、込められた思いに応えることが
出来ず、大変申し訳なく思っております。
ぜひ次の機会にもご提案いただければ幸いです。

```html
<!DOCTYPE html>
<html lang="en">
<head>
<meta charset="utf-8">
<title>Flower Catalogue vol.52</title>
<link href="https://fonts.googleapis.com/css2?family=Cormorant+Garamond:ital,wght@0,400;1,400&family=Pinyon+Script&display=swap" rel="stylesheet">
<style>
  :root {
    --page-width: 846px;
    --page-height: 1200px;
    --sage-light: #e6ead2;
    --sage: #b9c49a;
    --cream: #f2efdc;
    --bloom-plum: #7a3a45;
    --bloom-mauve: #b07d96;
    --band-magenta: rgba(196, 38, 92, 0.62);
    --title-white: #ffffff;
  }
  * { margin: 0; padding: 0; box-sizing: border-box; }
  html, body {
    width: var(--page-width);
    height: var(--page-height);
    overflow: hidden;
    background: #ffffff;
  }
  .cover {
    position: relative;
    width: var(--page-width);
    height: var(--page-height);
    overflow: hidden;
  }
  .cover-photo {
    position: absolute;
    inset: 0;
    background:
      radial-gradient(ellipse 260px 200px at 120px 560px, rgba(122, 58, 69, 0.45), transparent 70%),
      radial-gradient(ellipse 220px 180px at 80px 1040px, rgba(122, 58, 69, 0.4), transparent 70%),
      radial-gradient(ellipse 240px 220px at 420px 700px, rgba(176, 125, 150, 0.4), transparent 70%),
      radial-gradient(ellipse 300px 240px at 700px 640px, rgba(176, 125, 150, 0.35), transparent 70%),
      radial-gradient(ellipse 280px 220px at 520px 1080px, rgba(242, 239, 220, 0.8), transparent 70%),
      radial-gradient(ellipse 300px 240px at 330px 100px, rgba(242, 239, 220, 0.85), transparent 70%),
      linear-gradient(160deg, var(--sage-light) 0%, var(--sage) 50%, var(--sage-light) 100%);
  }
  .accent-band {
    position: absolute;
    top: 0;
    left: 550px;
    width: 212px;
    height: 100%;
    background: var(--band-magenta);
  }
  .title {
    position: absolute;
    inset: 0;
    color: var(--title-white);
    font-weight: 400;
    text-shadow: 0 0 6px rgba(90, 30, 40, 0.25);
  }
  .title .title-line { display: block; }
  .title .initial {
    position: absolute;
    font-family: "Pinyon Script", cursive;
    line-height: 1;
  }
  .title .word {
    position: absolute;
    font-family: "Cormorant Garamond", serif;
    font-style: italic;
    line-height: 1;
    white-space: nowrap;
  }
  .title .initial-f { left: 453px; top: 40px; font-size: 270px; }
  .title .word-flower { left: 556px; top: 236px; font-size: 66px; }
  .title .initial-c { left: 80px; top: 105px; font-size: 350px; }
  .title .word-catalogue { left: 268px; top: 298px; font-size: 110px; }
  .issue {
    position: absolute;
    left: 553px;
    top: 595px;
    color: var(--title-white);
    font-family: "Cormorant Garamond", serif;
    line-height: 1;
    white-space: nowrap;
  }
  .issue .issue-label { font-size: 68px; }
  .issue .issue-number { font-size: 125px; }
</style>
</head>
<body>
  <main class="cover">
    <div class="cover-photo" role="img" aria-label="Close-up photograph of pale cream and deep plum spider-petalled flowers among soft green foliage"></div>
    <div class="accent-band"></div>
    <h1 class="title">
      <span class="title-line"><span class="initial initial-f">F</span><span class="word word-flower">lower</span></span>
      <span class="title-line"><span class="initial initial-c">C</span><span class="word word-catalogue">atalogue</span></span>
    </h1>
    <p class="issue"><span class="issue-label">vol.</span><span class="issue-number">52</span></p>
  </main>
</body>
</html>
```